Permanent Makeup (cosmetics salon) Brochure

We need a 2-4 sites brochure for our Permanent Makeup (cosmetics salon). Our company is based in Austria / Vienna. -> Our homepage is www.mk-lorenzhuber.at
This brochure should show which treatments we provide ot our customers.

I've uploaded our old brochure, the content (text) would be nearly the same (look form "Must Haves", pics have to be new (look uploaded pics)
The old brochure is to dark. -> look for our homepage maybe you can make it like this

Target Market(s)

woman, age 25-70 years who wants to have permanent makeup on eyebrows, lips or eyeliner

Industry/Entity Type

Beauty Salon

Requirements
Must have
• pics which are uploaded.

*This text (somithing about our business)
"Für Frau Lorenzhuber ist Permanent Makeup ein Kunsthandwerk. Das Team von MK-Lorenzhuber ist spezialisiert auf natürliches Permanent Makeup damit der individuelle Typ jeder Kundin am schönsten zum Ausdruck kommt."

*We do this treatments: (english)
+ Augenbrauen Microblading (eyebrows)
+ Augenbrauen Permanent Makeup (eyebrows2)
+ Lidstrich Permanent Makeup (eyeliner)
+ Lip Blushing (lips)
+ Lippen Permanent Makeup (lips2)

* Our addresses (2 locations)
Wien
Kerngasse 7b/12, 1010 Wien
Tel: 01/5827316

Villach
Birkenhofweg 24, 9524 St. Ulrich
Tel: 0676/3158940

Mail: info@mk-lorenzhuber.at
www.mk-lorenzhuber.at

```html
<!DOCTYPE html>
<html lang="de">
<head>
<meta charset="utf-8">
<title>Marija Lorenzhuber Kosmetikstudio – Broschüre</title>
<link href="https://fonts.googleapis.com/css2?family=Josefin+Sans:wght@300;400&family=Oswald:wght@200&family=Open+Sans:wght@400;600&display=swap" rel="stylesheet">
<style>
  :root{
    --navy:#2b3654;
    --navy-light:#4b5668;
    --gold:#e3bf5f;
    --paper:#eeeff1;
    --ink:#3a3d45;
    --white:#ffffff;
    --backdrop:#8a8886;
    --skin:#d7a88e;
    --skin-dark:#a7745c;
  }
  *{margin:0;padding:0;box-sizing:border-box}
  html,body{width:1200px;height:1194px;overflow:hidden}
  body{background:var(--backdrop);position:relative;font-family:"Josefin Sans",sans-serif}
  .spread{position:absolute;left:181px;width:880px;height:441px;display:flex;box-shadow:0 4px 14px rgba(0,0,0,.25)}
  .spread--outer{top:134px}
  .spread--inner{top:610px}
  .page{position:relative;width:440px;height:441px;overflow:hidden}
  .abs{position:absolute}
  .navy-bg{background:linear-gradient(180deg,var(--navy) 0%,var(--navy-light) 100%)}
  .photo{position:absolute}
  .brand{position:absolute;left:0;right:0;text-align:center;font-family:"Josefin Sans",sans-serif;font-weight:300;letter-spacing:.5px}
  .brand--light{color:var(--white);font-size:19px;top:62px}
  .brand--dark{color:var(--ink);font-size:19px;top:380px}
  .brand-sub{position:absolute;left:0;right:0;text-align:center;font-size:6.5px;letter-spacing:3.5px;color:var(--white);top:95px}
  .tagline{position:absolute;left:0;right:0;text-align:center;font-family:"Open Sans",sans-serif;font-weight:600;font-size:6px;letter-spacing:.5px;color:var(--ink);top:406px}
  .intro{position:absolute;left:60px;right:60px;top:130px;text-align:center;color:var(--gold);font-weight:300;font-size:14px;line-height:18px}
  .bubble{position:absolute;border-radius:50%;border:3px solid var(--gold)}
  .contact{position:absolute;top:358px;font-family:"Open Sans",sans-serif;font-size:7.6px;color:var(--ink);line-height:11px}
  .contact__city{color:var(--gold);font-family:"Josefin Sans",sans-serif;font-size:9px;margin-bottom:2px}
  .contact__row{display:flex;align-items:center;gap:4px}
  .contact__row svg{width:7px;height:7px;fill:var(--ink)}
  .divider{position:absolute;left:214px;top:345px;width:1px;height:70px;background:#c9cacd}
  .claim{position:absolute;left:272px;top:116px;width:122px;color:var(--white);text-align:center}
  .claim__big{font-family:"Oswald",sans-serif;font-weight:200;font-size:35px;line-height:40px;text-align:left}
  .claim__line{font-weight:300;font-size:15px;letter-spacing:1px;text-align:left;margin-top:2px}
  .claim__von{display:flex;align-items:center;justify-content:space-between;font-size:16px;font-weight:300;margin-top:6px}
  .claim__von span{height:1px;width:34px;background:var(--gold)}
  .claim__innen{font-size:28px;letter-spacing:2px;font-weight:300;line-height:28px}
  .pill{display:inline-block;margin-top:6px;background:var(--gold);color:var(--white);font-size:7px;padding:3px 18px 2px;border-radius:6px;white-space:nowrap}
  .about__head{position:absolute;left:0;right:0;top:274px;text-align:center;color:var(--gold);font-size:13.5px;letter-spacing:.5px}
  .about__text{position:absolute;left:30px;right:30px;top:300px;text-align:center;color:var(--ink);font-weight:300;font-size:12px;line-height:20.6px}
  .booking{position:absolute;left:0;right:0;top:400px;height:24px;background:var(--navy-light);color:var(--white);font-weight:300;font-size:12px;display:flex;align-items:center;justify-content:center;gap:8px}
  .booking__dot{width:7px;height:7px;border-radius:50%;border:1.5px solid var(--gold)}
  .booking__url{color:var(--gold)}
  .treatments__tab{position:absolute;left:0;top:33px;width:229px;height:23px;background:var(--gold);border-radius:0 12px 12px 0;color:var(--navy);font-size:14px;padding:5px 0 0 34px;letter-spacing:.3px}
  .treatment{position:absolute;display:flex;align-items:center;gap:14px;color:var(--white);font-weight:300;font-size:9.3px;line-height:13.5px;letter-spacing:.3px}
  .treatment__pic{width:52px;height:52px;border-radius:50%;border:2px solid var(--gold);flex:none}
</style>
</head>
<body>

<section class="spread spread--outer">
  <!-- back cover -->
  <div class="page navy-bg">
    <div class="brand brand--light">Marija Lorenzhuber</div>
    <div class="brand-sub">KOSMETIKSTUDIO</div>
    <p class="intro">Ihr Kosmetikstudio und Beauty Salon in 1010<br>Wien Professionelles Microblading und Permanent<br>Make Up für gehobene Ansprüche</p>
    <svg class="abs" style="left:0;top:0" width="440" height="441" viewBox="0 0 440 441">
      <path d="M0 285 Q60 260 120 262 L120 268 Q60 268 0 333Z" fill="var(--gold)"/>
      <path d="M0 333 Q60 268 120 266 L300 285 L440 305 L440 441 L0 441Z" fill="var(--paper)"/>
    </svg>
    <div class="bubble photo" role="img" aria-label="Nahaufnahme eines Auges mit Permanent-Lidstrich" style="left:76px;top:216px;width:94px;height:94px;background:radial-gradient(circle,#6f8f83 0%,#c9a896 40%,#e2c6b6 100%)"></div>
    <div class="bubble photo" role="img" aria-label="Nahaufnahme eines Auges mit Augenbraue" style="left:266px;top:216px;width:94px;height:94px;background:radial-gradient(circle,#5b4032 0%,#caa08a 45%,#e6cbbd 100%)"></div>
    <div class="bubble photo" role="img" aria-label="Nahaufnahme von Lippen mit Permanent Makeup" style="left:157px;top:208px;width:118px;height:118px;background:radial-gradient(ellipse at 50% 50%,#e2858a 0%,#d87f80 35%,#e7b6a6 70%,#edc9bb 100%)"></div>
    <div class="divider"></div>
    <div class="contact" style="left:68px">
      <div class="contact__city">WIEN</div>
      <div class="contact__row"><svg viewBox="0 0 10 10"><path d="M5 0a3.5 3.5 0 0 0-3.5 3.5C1.5 6 5 10 5 10s3.5-4 3.5-6.5A3.5 3.5 0 0 0 5 0zm0 5a1.4 1.4 0 1 1 0-2.8A1.4 1.4 0 0 1 5 5z"/></svg>Kerngasse 7b/12, 1010 Wien</div>
      <div class="contact__row"><svg viewBox="0 0 10 10"><path d="M2 0l2 2.5-1 1.2a6 6 0 0 0 3.3 3.3l1.2-1L10 8l-1.5 2C4 10 0 6 0 1.5z"/></svg>01/5827316</div>
      <div class="contact__row"><svg viewBox="0 0 10 10"><path d="M0 2h10v6H0zm1 1v.3l4 2.5 4-2.5V3z"/></svg>info@mk-lorenzhuber.at</div>
    </div>
    <div class="contact" style="left:255px">
      <div class="contact__city">VILLACH</div>
      <div class="contact__row"><svg viewBox="0 0 10 10"><path d="M5 0a3.5 3.5 0 0 0-3.5 3.5C1.5 6 5 10 5 10s3.5-4 3.5-6.5A3.5 3.5 0 0 0 5 0zm0 5a1.4 1.4 0 1 1 0-2.8A1.4 1.4 0 0 1 5 5z"/></svg>Birkenhofweg 24, 9524 St. Ulrich</div>
      <div class="contact__row"><svg viewBox="0 0 10 10"><path d="M2 0l2 2.5-1 1.2a6 6 0 0 0 3.3 3.3l1.2-1L10 8l-1.5 2C4 10 0 6 0 1.5z"/></svg>0676/3158940</div>
      <div class="contact__row"><svg viewBox="0 0 10 10"><path d="M0 2h10v6H0zm1 1v.3l4 2.5 4-2.5V3z"/></svg>info@mk-lorenzhuber.at</div>
    </div>
  </div>

  <!-- front cover -->
  <div class="page navy-bg">
    <div class="photo" role="img" aria-label="Porträtfoto einer jungen Frau mit natürlichem Make-up, Hand am Kinn" style="left:0;top:0;width:256px;height:360px;background:linear-gradient(100deg,var(--skin-dark) 0%,var(--skin) 45%,#c9a493 75%,#7f8da0 100%)"></div>
    <div class="claim">
      <div class="claim__big">SCHÖNHEIT</div>
      <div class="claim__line">kommt nicht nur</div>
      <div class="claim__von"><span></span>von<span></span></div>
      <div class="claim__innen">innen</div>
      <div class="pill">www.mk-lorenzhuber.at</div>
    </div>
    <svg class="abs" style="left:0;top:0" width="440" height="441" viewBox="0 0 440 441">
      <path d="M0 305 Q170 350 300 345 Q400 340 440 292 L440 310 Q400 345 300 348 Q170 352 0 305Z" fill="var(--gold)"/>
      <path d="M0 305 Q170 352 300 349 Q400 346 440 318 L440 441 L0 441Z" fill="var(--paper)"/>
    </svg>
    <div class="brand brand--dark">Marija Lorenzhuber</div>
    <div class="tagline">WAS IHNEN WERTVOLL IST, GEHÖRT IN GUTE HÄNDE</div>
  </div>
</section>

<section class="spread spread--inner">
  <!-- about page -->
  <div class="page" style="background:var(--paper)">
    <div class="photo" role="img" aria-label="Nahaufnahme eines Frauenauges mit Augenbraue und hellem Haar" style="left:0;top:0;width:440px;height:260px;background:linear-gradient(160deg,#e9d2c4 0%,#d9b3a1 40%,#b9927f 70%,#e6d3c5 100%);clip-path:path('M0 0 L418 0 Q400 200 0 250Z')"></div>
    <svg class="abs" style="left:0;top:0" width="440" height="441" viewBox="0 0 440 441">
      <path d="M418 0 Q400 200 0 250" fill="none" stroke="var(--white)" stroke-width="6"/>
      <path d="M427 0 Q410 210 0 257" fill="none" stroke="var(--gold)" stroke-width="4"/>
    </svg>
    <div class="about__head">IHR KOSMETIKSTUDIO UND BEAUTY SALON</div>
    <p class="about__text">Für Frau Lorenzhuber ist Permanent Makeup ein Kunsthandwerk.<br>Das Team von MK-Lorenzhuber ist spezialisiert auf natürliches<br>Permanent Makeup damit der individuelle Typ jeder Kundin am<br>schönsten zum Ausdruck kommt.</p>
    <div class="booking">Online Termin vereinbaren <span class="booking__dot"></span> <span class="booking__url">www.mk-lorenzhuber.at</span></div>
  </div>

  <!-- treatments page -->
  <div class="page navy-bg">
    <div class="treatments__tab">WE DO THIS TREATMENTS</div>
    <div class="treatment" style="left:36px;top:70px"><div class="treatment__pic" role="img" aria-label="Augenbraue nach Microblading" style="background:radial-gradient(circle,#5a463c,#d7b3a0 60%,#e8cfc2)"></div>Augenbrauen Microblading<br>(eyebrows)</div>
    <div class="treatment" style="left:251px;top:70px"><div class="treatment__pic" role="img" aria-label="Augenbraue mit Permanent Makeup" style="background:radial-gradient(circle,#7a6a66,#d9b6a5 60%,#ebd3c6)"></div>Augenbrauen Permanent<br>Makeup (eyebrows2)</div>
    <div class="treatment" style="left:36px;top:136px"><div class="treatment__pic" role="img" aria-label="Auge mit Permanent-Lidstrich" style="background:radial-gradient(circle,#4b3a30,#cfa792 60%,#e6cbbd)"></div>Lidstrich Permanent<br>Makeup (eyeliner)</div>
    <div class="treatment" style="left:251px;top:136px"><div class="treatment__pic" role="img" aria-label="Lippen in Nahaufnahme" style="background:radial-gradient(ellipse,#d57b7c,#e3a59a 60%,#edc6b8)"></div>Microfeathering<br>Augenbrauen</div>
    <div class="treatment" style="left:36px;top:202px"><div class="treatment__pic" role="img" aria-label="Grünes Auge mit Lidstrich" style="background:radial-gradient(circle,#6f8f83,#c9a896 55%,#e2c6b6)"></div>Lippen Permanent<br>Makeup (lips2)</div>
    <div class="treatment" style="left:251px;top:202px"><div class="treatment__pic" role="img" aria-label="Lippen nach Lip Blushing" style="background:radial-gradient(ellipse,#d9797d,#e4a39b 60%,#efc9bc)"></div>Lip Blushing<br>(lips)</div>
    <div class="photo" role="img" aria-label="Porträtfoto einer Frau mit langem braunem Haar" style="left:0;top:0;width:440px;height:441px;background:linear-gradient(100deg,#6b5446 20%,#c99a80 50%,#d8ae95 70%,#5f6d78 100%);clip-path:path('M20 441 Q120 300 440 265 L440 441Z')"></div>
    <svg class="abs" style="left:0;top:0" width="440" height="441" viewBox="0 0 440 441">
      <path d="M20 441 Q120 300 440 265" fill="none" stroke="var(--white)" stroke-width="4"/>
      <path d="M12 441 Q112 294 440 259" fill="none" stroke="var(--gold)" stroke-width="4"/>
    </svg>
  </div>
</section>

</body>
</html>
```